Bright Oak Family Dentistry
Logo For Dental Office - Medical
Logo For Dental Office
Professional
Mira Tolvanen
DMD
2687 Pemberly Lane Suite 214 Virginia Beach, VA 23461
brightoak482@mailnest.com
brightoakfamilydentistry.com
I would like shades of blue in my logo
Appointment card on the back
kivo-darrel kivo-darrel
Can you give me an existing copy of your logo.
lumengrit lumengrit
Hello sir, Can you please provide your logo? :)

```html
<!DOCTYPE html>
<html lang="en">
<head>
<meta charset="utf-8">
<title>Bright Oak Family Dentistry – Business Card</title>
<link href="https://fonts.googleapis.com/css2?family=EB+Garamond:wght@400;500&display=swap" rel="stylesheet">
<style>
  :root {
    --brand-blue: #1d86c6;
    --swoosh-grey: #a4a6a8;
    --ink: #231f20;
    --paper: #ffffff;
  }
  html, body {
    margin: 0;
    padding: 0;
    width: 1200px;
    height: 756px;
    overflow: hidden;
    background: var(--paper);
  }
  .card {
    position: relative;
    width: 1200px;
    height: 756px;
    background: var(--paper);
    font-family: "EB Garamond", Georgia, serif;
    color: var(--ink);
  }
  .header-art {
    position: absolute;
    left: 0;
    top: 0;
    width: 1200px;
    height: 756px;
  }
  .header-band { fill: var(--brand-blue); }
  .header-swoosh { fill: var(--swoosh-grey); }
  .footer-band { fill: var(--brand-blue); }

  .brand {
    position: absolute;
    left: 293px;
    top: 192px;
    color: var(--paper);
    font-weight: 400;
    line-height: 1;
  }
  .brand-mark {
    position: absolute;
    left: -30px;
    top: -14px;
    width: 18px;
    height: 18px;
    border-radius: 50%;
    background: var(--paper);
  }
  .brand-name {
    display: block;
    font-size: 48px;
    letter-spacing: 1px;
    text-transform: uppercase;
  }
  .brand-tagline {
    display: block;
    font-size: 30px;
    margin-top: 0;
    padding-left: 50px;
    letter-spacing: 0.5px;
  }

  .practitioner {
    position: absolute;
    left: 552px;
    top: 358px;
    margin: 0;
    font-weight: 400;
    font-size: 58px;
    letter-spacing: 1px;
    line-height: 1;
  }
  .credential {
    font-size: 34px;
    letter-spacing: 1px;
    margin-left: 6px;
  }

  .address {
    position: absolute;
    left: 160px;
    top: 466px;
    margin: 0;
    font-style: normal;
    font-size: 29px;
    line-height: 36px;
  }
  .contact {
    position: absolute;
    left: 618px;
    top: 530px;
    margin: 0;
    font-size: 26px;
    line-height: 36px;
  }
  .contact p, .address p { margin: 0; }
</style>
</head>
<body>
  <main class="card">
    <svg class="header-art" viewBox="0 0 1200 756" aria-hidden="true">
      <path class="header-band" d="M137 108 H1063 V180 C880 285 550 312 137 312 Z"/>
      <path class="header-swoosh" d="M560 322 C760 306 940 258 1063 190 L1063 204 C940 266 760 310 560 322 Z"/>
      <path class="header-swoosh" d="M700 318 C850 304 960 270 1063 214 L1063 219 C960 275 850 308 700 318 Z"/>
      <rect class="footer-band" x="137" y="612" width="926" height="31"/>
    </svg>

    <div class="brand">
      <span class="brand-mark"></span>
      <span class="brand-name">Bright Oak</span>
      <span class="brand-tagline">Family Dentistry</span>
    </div>

    <h1 class="practitioner">Mira Tolvanen<span class="credential">DMD</span></h1>

    <address class="address">
      <p>2687 Pemberly Lane</p>
      <p>Suite 214, Virginia Beach,</p>
      <p>VA 23461</p>
      <p>Ph: 757-555-0148</p>
    </address>

    <div class="contact">
      <p>Email: brightoak482@mailnest.com</p>
      <p>www.brightoakfamilydentistry.com</p>
    </div>
  </main>
</body>
</html>
```